Wedding Dried Apple Label / Name Place Card

We are looking for a simple but stylish label to be attached via string to a bag of dried apples from my family's fruit farm. The size of the label we think should be similar to the size of a business card. The packaging will be a plastic bag: 4" x 2" x 6".
We would like it to say something like:
Remy & Joss
Est. Sept 10, 2017
Dried Apple Slices
Product of Quenton Fruit Farm
________________
(We need a spot to write in the name of the person and a table number)
Our colors are also grey and navy, and would like these colors to be used.
We have uploaded a photo of the plastic bag.
Wedding

```html
<!DOCTYPE html>
<html lang="en">
<head>
<meta charset="utf-8">
<title>Remy &amp; Joss – Dried Apple Slices Label</title>
<link rel="stylesheet" href="https://fonts.googleapis.com/css2?family=Montserrat:wght@400;500&family=Oswald:wght@400;500&display=swap">
<style>
  :root {
    --navy: #22528a;
    --grey: #b3b3b3;
    --white: #ffffff;
    --apple: #d9322b;
    --leaf: #bdbdbd;
  }
  html, body {
    margin: 0;
    padding: 0;
    width: 686px;
    height: 1200px;
    overflow: hidden;
    background: var(--white);
  }
  .label {
    position: relative;
    width: 686px;
    height: 1200px;
    font-family: "Oswald", sans-serif;
  }
  .label-art {
    position: absolute;
    inset: 0;
  }
  .couple-names {
    position: absolute;
    left: 44px;
    top: 233px;
    width: 596px;
    height: 73px;
    margin: 0;
    display: flex;
    align-items: center;
    justify-content: center;
    font-family: "Montserrat", sans-serif;
    font-weight: 400;
    font-size: 50px;
    letter-spacing: 9px;
    color: var(--white);
  }
  .established {
    position: absolute;
    left: 0;
    top: 317px;
    width: 686px;
    margin: 0;
    text-align: center;
    font-weight: 500;
    font-size: 33px;
    letter-spacing: 6px;
    color: var(--grey);
  }
  .product-name {
    position: absolute;
    left: 118px;
    top: 405px;
    width: 448px;
    height: 72px;
    margin: 0;
    display: flex;
    align-items: center;
    justify-content: center;
    font-weight: 500;
    font-size: 31px;
    letter-spacing: 6px;
    color: var(--white);
  }
  .origin-heading {
    position: absolute;
    left: 0;
    top: 576px;
    width: 686px;
    margin: 0;
    text-align: center;
    font-weight: 500;
    font-size: 26px;
    letter-spacing: 6px;
    color: var(--grey);
  }
  .table-number {
    position: absolute;
    left: 124px;
    top: 880px;
    margin: 0;
    font-weight: 500;
    font-size: 29px;
    letter-spacing: 6px;
    color: var(--grey);
  }
  .farm-name {
    font-family: "Montserrat", sans-serif;
    font-weight: 500;
    font-size: 23px;
    letter-spacing: 3px;
    fill: var(--white);
  }
</style>
</head>
<body>
<main class="label">
  <svg class="label-art" width="686" height="1200" viewBox="0 0 686 1200" xmlns="http://www.w3.org/2000/svg">
    <!-- outer frame -->
    <rect x="23" y="30" width="638" height="1137" rx="24" fill="none" stroke="var(--navy)" stroke-width="8"/>

    <!-- crest ornament placeholders -->
    <rect x="64" y="72" width="240" height="120" rx="40" fill="var(--leaf)" role="img" aria-label="Grey laurel branch reaching toward the apple"/>
    <rect x="382" y="72" width="240" height="120" rx="40" fill="var(--leaf)" role="img" aria-label="Grey laurel branch reaching toward the apple"/>
    <rect x="311" y="130" width="64" height="78" rx="28" fill="var(--apple)" role="img" aria-label="Red apple with green leaf"/>

    <!-- names band -->
    <rect x="44" y="233" width="596" height="73" fill="var(--navy)"/>

    <!-- product ribbon -->
    <polygon points="41,429 112,429 112,485 41,485 82,457" fill="var(--navy)"/>
    <polygon points="645,429 574,429 574,485 645,485 604,457" fill="var(--navy)"/>
    <rect x="112" y="474" width="63" height="11" fill="var(--navy)"/>
    <rect x="508" y="474" width="66" height="11" fill="var(--navy)"/>
    <rect x="118" y="405" width="448" height="72" fill="var(--navy)" stroke="var(--white)" stroke-width="3"/>

    <!-- origin panel -->
    <rect x="48" y="558" width="590" height="402" rx="86" fill="none" stroke="var(--grey)" stroke-width="9"/>

    <!-- farm ribbon -->
    <polygon points="112,712 65,738 92,745 65,802 150,760 112,745" fill="var(--navy)"/>
    <polygon points="574,712 621,738 594,745 621,802 536,760 574,745" fill="var(--navy)"/>
    <path d="M112 677 Q343 559 571 677 L571 737 Q343 627 112 737 Z" fill="var(--navy)" stroke="var(--white)" stroke-width="3"/>
    <path id="farm-arc" d="M100 712 Q343 600 586 712" fill="none"/>
    <text class="farm-name" text-anchor="middle"><textPath href="#farm-arc" startOffset="50%">• QUENTON FRUIT FARM •</textPath></text>

    <!-- write-in lines -->
    <line x1="110" y1="842" x2="571" y2="842" stroke="var(--grey)" stroke-width="2"/>
    <line x1="317" y1="917" x2="538" y2="917" stroke="var(--grey)" stroke-width="2"/>

    <!-- footer ornament placeholder -->
    <rect x="120" y="1032" width="442" height="90" rx="45" fill="var(--leaf)" role="img" aria-label="Crossed grey branch flourish"/>
  </svg>

  <h1 class="couple-names">REMY &amp; JOSS</h1>
  <p class="established">EST. SEPTEMBER•10•2017</p>
  <h2 class="product-name">DRIED APPLE SLICES</h2>
  <p class="origin-heading">PRODUCT OF:</p>
  <p class="table-number">TABLE Nº:</p>
</main>
</body>
</html>
```